IT Services Business Card Design

We require a business card design for an IT services company called RT Code Transit.

We specialize in taking an organisations software and readying it for deployment to new environments (e.g. Nex 3 to Nex 5). This process is termed application packaging. This is not the same as putting things in boxes but I am happy to use boxes as a pun icon ;-) This is our second step in branding, we currently have a new logo and our poor excuse of a website is next to be updated but it contains information on who we are and what we cover at rtcodetransit.example

We are looking for a fun, modern but stylish and professional looking design.

I have attached the logo in multiple formats including vector formats (and the fonts that created the logo if required)
Updates

Thanks to all the designers so far, some great designs in there.  I will be selecting a card design on the deadline date. 

However, there is still time to submit some more designs.  The majority of the ones I have so far are typical simplistic designs that we have all seen before and I have enough of those to choose from now.  If you wish to submit any more designs, please submit somthing unusual to grab our attention.

Target Market(s)

Project executives of large organisations looking for Nexora migrations

Industry/Entity Type

Software

Requirements
Must have
• Want to show company name, contact name, title, main number, contact number, fax number, email address and website address. I do not want to show the address.
Must use the attached logo, retaining the colours in them.

This has to be a double-sided design. I will be using pelby.example and will be selecting their rounded corner business card design.

Their templates and design requirements (sizing etc.) can be found here: http://uk.pelby.example/help/faq/templates-and-guidelines.html

Happy for company name or website to be on either side of the card.

This design has to be original and not used before for another company

Would like to style it around the business colours in the logo
Nice to have
• Pelby.example has an option for multiple card designs to appear on the back. If this is possible in the budget and time you have and you have a design(s) that work with that but carry the same style and theme, that would be nice to see but not necessary.
Should not have
• We do not want to put a postal address on the cards

```html
<!DOCTYPE html>
<html lang="en">
<head>
<meta charset="utf-8">
<title>RT Code Transit – Business Card</title>
<link rel="stylesheet" href="https://fonts.googleapis.com/css2?family=Open+Sans:wght@400;600;700&family=Questrial&display=swap">
<style>
  :root {
    --stage: #2b2b2b;
    --card-white: #ffffff;
    --card-dark: #2f332f;
    --card-dark-edge: #3a3f3a;
    --brand-blue: #4f6fdc;
    --brand-blue-light: #7f96e6;
    --ink: #333333;
    --ink-soft: #666666;
    --on-dark: #e6e6e6;
  }
  * { box-sizing: border-box; margin: 0; padding: 0; }
  html, body { width: 1200px; height: 900px; overflow: hidden; }
  body {
    background: var(--stage);
    display: flex;
    flex-direction: column;
    align-items: center;
    justify-content: center;
    gap: 40px;
    font-family: "Open Sans", Arial, sans-serif;
  }
  .card {
    position: relative;
    width: 540px;
    height: 330px;
    border-radius: 14px;
    overflow: hidden;
    box-shadow: 0 10px 30px rgba(0,0,0,.45);
  }

  /* Front */
  .card--front { background: var(--card-white); color: var(--ink); }
  .card__swoosh { position: absolute; left: 0; top: 0; width: 100%; height: 100%; }
  .brand {
    position: absolute;
    display: flex;
    align-items: center;
    gap: 10px;
    font-family: "Questrial", Arial, sans-serif;
    white-space: nowrap;
  }
  .brand__dot { border-radius: 50%; background: var(--brand-blue); flex: none; }
  .card--front .brand { left: 36px; top: 118px; font-size: 26px; color: #555555; }
  .card--front .brand__dot { width: 28px; height: 28px; }

  .person { position: absolute; right: 36px; top: 32px; text-align: right; }
  .person__name { font-weight: 700; font-size: 18px; color: var(--brand-blue); letter-spacing: .5px; }
  .person__title { font-size: 11px; color: var(--ink-soft); }

  .contact-list { position: absolute; right: 36px; top: 96px; list-style: none; }
  .contact-list li {
    display: flex; justify-content: flex-end; align-items: center; gap: 6px;
    font-size: 12px; line-height: 18px; color: var(--ink);
  }
  .contact-list svg { width: 11px; height: 11px; fill: var(--brand-blue); }

  .web-lines { position: absolute; right: 36px; top: 176px; text-align: right; font-size: 13px; line-height: 18px; color: var(--ink); }

  /* Back */
  .card--back {
    background: linear-gradient(160deg, var(--card-dark-edge) 0%, var(--card-dark) 55%, #292c29 100%);
    color: var(--on-dark);
  }
  .card--back .brand { left: 70px; top: 120px; font-size: 40px; color: var(--on-dark); }
  .card--back .brand__dot { width: 90px; height: 90px; margin-left: 30px; }
  .card__url { position: absolute; left: 70px; bottom: 60px; font-size: 15px; letter-spacing: 1.5px; color: var(--on-dark); }
</style>
</head>
<body>

  <section class="card card--front" aria-label="Card front">
    <svg class="card__swoosh" viewBox="0 0 540 330" preserveAspectRatio="none" aria-hidden="true">
      <path d="M0 284 Q300 272 540 226 L540 330 L0 330 Z" fill="var(--brand-blue-light)"/>
      <path d="M0 298 Q300 287 540 244 L540 330 L0 330 Z" fill="var(--brand-blue)"/>
      <path d="M0 318 Q300 306 540 266 L540 330 L0 330 Z" fill="var(--card-white)"/>
    </svg>

    <div class="brand"><span class="brand__dot"></span>RT Code Transit</div>

    <div class="person">
      <p class="person__name">TAM HOLLIS</p>
      <p class="person__title">General Manager</p>
    </div>

    <ul class="contact-list">
      <li>0800 555 0142
        <svg viewBox="0 0 12 12"><path d="M3 1l2 2.5-1 1.2a6 6 0 0 0 3.3 3.3l1.2-1L11 9l-1 2C5 11 1 7 1 2z"/></svg></li>
      <li>0800 555 0178
        <svg viewBox="0 0 12 12"><rect x="3" y="1" width="6" height="3"/><rect x="1" y="4.5" width="10" height="4.5" rx="1"/><rect x="3" y="8" width="6" height="3"/></svg></li>
      <li>RTCodeTransit.example
        <svg viewBox="0 0 12 12"><rect x="1" y="2.5" width="10" height="7" rx="1"/><path d="M1.5 3l4.5 3.5L10.5 3" stroke="#fff" fill="none"/></svg></li>
      <li>RTCodeTransit.example
        <svg viewBox="0 0 12 12"><circle cx="6" cy="6" r="5"/><path d="M1 6h10M6 1c2.5 3 2.5 7 0 10M6 1c-2.5 3-2.5 7 0 10" stroke="#fff" stroke-width=".8" fill="none"/></svg></li>
    </ul>

    <div class="web-lines">
      <p>Enquiries@RTCodeTransit.example</p>
      <p>www.RTCodeTransit.example</p>
    </div>
  </section>

  <section class="card card--back" aria-label="Card back">
    <div class="brand">RT Code Transit<span class="brand__dot"></span></div>
    <p class="card__url">www.rtcodetransit.example</p>
  </section>

</body>
</html>
```